We need a completed book cover (front and back) for a Christian devotional book titled "Walking Steady Onward: Shaped as an Open PATH Follower" by Dr. Martin Hale. The publishing company should be "Open Path" (https://opnpathhub.org). This will be for small groups to go through together daily to understand how to grow as a Christian as a part of the family of God. I'm attaching the Open Path logo and the introduction to the book.
Main themes include navigating today’s culture, understanding and using our spiritual gifts, and experiencing joy in community.

```html
<!DOCTYPE html>
<html lang="en">
<head>
<meta charset="utf-8">
<title>Walking Steady Onward – Book Cover</title>
<link rel="stylesheet" href="https://fonts.googleapis.com/css2?family=Bebas+Neue&family=Montserrat:wght@400;500&display=swap">
<style>
  :root {
    --navy: #0a2b4f;
    --white: #ffffff;
    --paper: #ffffff;
    --violet: #4a3fd6;
    --cyan: #5fe0f5;
    --sky-top: #4a4fe0;
    --sky-mid: #5ec4f2;
  }
  * { margin: 0; padding: 0; box-sizing: border-box; }
  html, body { width: 1200px; height: 1000px; overflow: hidden; background: var(--paper); }
  .canvas { position: relative; width: 1200px; height: 1000px; }

  .back-cover {
    position: absolute; left: 86px; top: 126px; width: 496px; height: 704px;
    background: var(--navy);
  }
  .back-frame {
    position: absolute; left: 21px; top: 26px; width: 455px; height: 654px;
    border: 2px solid var(--white);
  }
  .back-title {
    position: absolute; left: 0; right: 0; top: 72px; text-align: center;
    font-family: 'Bebas Neue', sans-serif; font-weight: 400; color: var(--white);
    font-size: 31px; letter-spacing: 2.4px; line-height: 1; white-space: nowrap;
  }
  .back-subtitle {
    position: absolute; left: 0; right: 0; top: 111px; text-align: center;
    font-family: 'Bebas Neue', sans-serif; font-weight: 400; color: var(--white);
    font-size: 15px; letter-spacing: 1.5px; line-height: 1; white-space: nowrap;
  }
  .back-intro {
    position: absolute; left: 71px; width: 410px;
    font-family: 'Montserrat', sans-serif; color: var(--white);
    font-size: 13.4px; line-height: 16.8px; white-space: pre-line;
  }
  .intro-lead { left: 73px; top: 162px; }
  .intro-story { top: 257px; }

  .spine {
    position: absolute; left: 584px; top: 126px; width: 49px; height: 704px;
    background: var(--navy);
  }
  .spine-title {
    position: absolute; left: 50%; top: 360px;
    transform: translate(-50%, -50%) rotate(90deg);
    white-space: nowrap; font-family: 'Montserrat', sans-serif;
    color: var(--white); font-size: 26px; letter-spacing: 5.6px; line-height: 1;
  }

  .front-cover {
    position: absolute; left: 635px; top: 126px; width: 494px; height: 704px;
    background: var(--navy); overflow: hidden;
  }
  .front-art {
    position: absolute; left: 0; top: 0; width: 494px; height: 370px;
    background: linear-gradient(180deg, var(--sky-top) 0%, #6a8ef0 30%, var(--sky-mid) 65%, #3a3ad0 100%);
  }
  .title-badge {
    position: absolute; left: 45px; top: 448px; width: 406px; height: 88px;
    transform: rotate(-3deg);
    background: linear-gradient(90deg, var(--violet) 0%, #5a7be8 55%, var(--cyan) 100%);
    border: 2px solid var(--white); border-radius: 6px;
    box-shadow: 0 4px 8px rgba(0,0,0,0.25);
  }
  .badge-title {
    position: absolute; left: 12px; top: 8px;
    font-family: 'Bebas Neue', sans-serif; font-weight: 400; color: var(--white);
    font-size: 50px; line-height: 1; letter-spacing: 0; white-space: nowrap;
  }
  .badge-subtitle {
    position: absolute; right: 14px; top: 58px;
    font-family: 'Montserrat', sans-serif; font-weight: 500; color: var(--white);
    font-size: 17px; line-height: 1; letter-spacing: 0.3px; white-space: nowrap;
  }
  .author {
    position: absolute; right: 30px; top: 640px;
    font-family: 'Montserrat', sans-serif; color: var(--white);
    font-size: 22px; white-space: nowrap;
  }
</style>
</head>
<body>
<div class="canvas">

  <section class="back-cover">
    <div class="back-frame"></div>
    <h1 class="back-title">Walking Steady Onward</h1>
    <h2 class="back-subtitle">Shaped as an Open PATH Follower</h2>
    <p class="back-intro intro-lead">If you take the time, God will speak to you and
your friends again and again through this daily
time in His word, the Bible.   These words may
help you bigtime in learning to listen to the
Lord of the Universe</p>
    <p class="back-intro intro-story">Daniel Oketch and I have partnered together in
 east Africa for close to 20 years, and we love to
take a concept and go deeper together on how
we communicate that principle to young leaders.
I brought the idea of Watch, Wait, and Listen to Daniel:
let's give people a simple means to think
more deeply about the biblical principles by using these
three action words.  Daniel, ever so gracious,
responded simply, "This is a wonderful approach to
helping people go deeper. May I suggest,
at least for Americans, that you add one more word
at the beginning."  My friend, ever so gentle in
his demeanor, suddenly yelled out the word:

"STOP!  So many Americans simple do not
know how to stop.  You appear to run from
activity to
activity, from meal to meal and from relationship
to relationship.  No, to make this three-step
principle real, you must actually do a FULL STOP
before you begin!"  A more piercing truth spoken
so directly I had not heard in many years, and
I was speechless.   We let the press of EVERYTHING
PRESS IN EVERYWHERE.</p>
  </section>

  <section class="spine">
    <span class="spine-title">CHRISTIAN DEVOTIONAL</span>
  </section>

  <section class="front-cover">
    <div class="front-art" role="img" aria-label="Illustration of three crosses silhouetted against a full moon over blue mountains"></div>
    <div class="title-badge">
      <span class="badge-title">CHRISTIAN DEVOTIONAL</span>
      <span class="badge-subtitle">Walking Steady Onward</span>
    </div>
    <p class="author">by Dr. Martin Hale</p>
  </section>

</div>
</body>
</html>
```